Real Estate Business card design

Company Name: Thornbury Holdings, LLC
subtitle: We pay cash for houses!
Martin Calloway
Managing Director
518-674-2913
Mart@ThornburyHoldingsLLC.example
www.ThornburyHoldingsLLC.example

We pay referral fees for Seller and Buyer leads.

Back:
We offer referral fees for Seller and Buyer leads that close.

Please contact Ned at 518-674-2913 with your referrals or to learn more about the referral program!

I am open to different color options but I am going for a classic, elegant, clean, and professional look. Please use logo as a reference.

Target Market(s)

People selling their homes and people in the market for buying homes.

Contact Information for Business Card

please see project description

Font styles to use
Serif
Sans Serif
Script

Requirements
Must have
• must have my logo in it
Nice to have
• I like cards that are split down the middle but please come up with a few mock ups. Open to any color scheme.

```html
<!DOCTYPE html>
<html lang="en">
<head>
<meta charset="UTF-8">
<title>Thornbury Holdings, LLC – Business Card</title>
<link href="https://fonts.googleapis.com/css2?family=Montserrat:ital,wght@0,400;0,500;0,600;0,700;1,400&display=swap" rel="stylesheet">
<style>
  :root {
    --backdrop: #d4d4d4;
    --slate: #474c57;
    --navy: #3d4454;
    --gold: #c2956a;
    --paper: #ffffff;
    --ink-light: #f2f2f2;
  }
  * { box-sizing: border-box; margin: 0; padding: 0; }
  html, body {
    width: 1200px; height: 900px; overflow: hidden;
    background: var(--backdrop);
    font-family: "Montserrat", Arial, sans-serif;
  }
  .sheet {
    width: 1200px; height: 900px;
    display: flex; flex-direction: column;
    align-items: center; justify-content: center; gap: 50px;
  }
  .card {
    position: relative;
    width: 660px; height: 377px;
    border-radius: 34px;
    overflow: hidden;
    box-shadow: 0 6px 18px rgba(0,0,0,0.18);
  }

  /* Back side */
  .card--back { background: var(--slate); color: var(--ink-light); text-align: center; }
  .card--back .brand {
    position: absolute; top: 92px; left: 0; right: 0;
    display: flex; align-items: center; justify-content: center; gap: 14px;
  }
  .brand__mark { width: 18px; height: 18px; background: var(--gold); }
  .brand__name { font-weight: 600; font-size: 34px; letter-spacing: 0.5px; }
  .card--back .brand__name { color: var(--paper); }
  .back__headline {
    position: absolute; top: 210px; left: 0; right: 0;
    color: var(--gold); font-weight: 700; font-size: 19px; letter-spacing: 0.4px;
  }
  .back__body {
    position: absolute; top: 258px; left: 70px; right: 70px;
    font-size: 17px; line-height: 1.5; letter-spacing: 0.3px;
  }
  .back__body strong { font-weight: 700; color: var(--paper); }

  /* Front side */
  .card--front { background: var(--paper); color: var(--navy); }
  .card--front .brand {
    position: absolute; top: 62px; left: 60px;
    display: flex; align-items: center; gap: 12px;
  }
  .card--front .brand__name { color: var(--navy); font-size: 30px; }
  .front__tagline {
    position: absolute; top: 118px; left: 60px;
    color: var(--gold); font-style: italic; font-size: 26px; letter-spacing: 0.5px;
  }
  .front__person {
    position: absolute; top: 196px; left: 60px;
    font-weight: 600; font-size: 26px; letter-spacing: 1px; text-transform: uppercase;
  }
  .contact-list {
    position: absolute; top: 246px; left: 60px;
    list-style: none; font-size: 16px; letter-spacing: 0.4px;
  }
  .contact-list li { display: flex; align-items: center; gap: 12px; height: 28px; }
  .contact-list svg { width: 18px; height: 18px; flex: none; }
  .front__referral {
    position: absolute; right: 50px; top: 170px; width: 240px;
    text-align: right; font-weight: 700; font-size: 17px; line-height: 1.35;
  }
</style>
</head>
<body>
<main class="sheet">

  <section class="card card--back" aria-label="Card back">
    <div class="brand">
      <span class="brand__mark"></span>
      <span class="brand__name">Thornbury Holdings, LLC</span>
    </div>
    <p class="back__headline">We offer referral fees for Seller and Buyer leads that close.</p>
    <p class="back__body">Please contact <strong>Ned</strong> at <strong>518-674-2913</strong> with your referrals or to learn more about the referral program!</p>
  </section>

  <section class="card card--front" aria-label="Card front">
    <div class="brand">
      <span class="brand__mark"></span>
      <span class="brand__name">Thornbury Holdings, LLC</span>
    </div>
    <p class="front__tagline">We pay cash for houses!</p>
    <h1 class="front__person">Martin Calloway</h1>
    <ul class="contact-list">
      <li>
        <svg viewBox="0 0 24 24" aria-hidden="true"><path fill="var(--gold)" d="M6.6 10.8a15.1 15.1 0 0 0 6.6 6.6l2.2-2.2a1 1 0 0 1 1-.25 11.4 11.4 0 0 0 3.6.57 1 1 0 0 1 1 1V20a1 1 0 0 1-1 1A17 17 0 0 1 3 4a1 1 0 0 1 1-1h3.5a1 1 0 0 1 1 1c0 1.25.2 2.45.57 3.57a1 1 0 0 1-.25 1z"/></svg>
        518-674-2913
      </li>
      <li>
        <svg viewBox="0 0 24 24" aria-hidden="true"><rect x="2" y="5" width="20" height="14" rx="1" fill="var(--gold)"/><path d="M2.5 5.5 12 13l9.5-7.5" fill="none" stroke="#fff" stroke-width="1.6"/></svg>
        Mart@ThornburyHoldingsLLC.example
      </li>
      <li>
        <svg viewBox="0 0 24 24" aria-hidden="true"><g fill="none" stroke="var(--gold)" stroke-width="1.8"><circle cx="12" cy="12" r="9"/><ellipse cx="12" cy="12" rx="4" ry="9"/><path d="M3 12h18M4.5 7.5h15M4.5 16.5h15"/></g></svg>
        www.ThornburyHoldingsLLC.example
      </li>
    </ul>
    <p class="front__referral">We pay referral fees for Seller and Buyer leads</p>
  </section>

</main>
</body>
</html>
```